Schnapsbrennerei sucht neue Etiketten
Zielgruppe
Wir sind eine örtliche Schnapsbrennerei, die inzwischen seit ein paar Jahren einen eigenen Kundenstamm aufgebaut hat. Nun werden wir im nächsten Jahr einen neuen Verkaufsraum bauen. Aus diesem Grund wollen wir unsere Etiketten komplett überarbeiten.
Ein neues Logo habe ich bereits designen lassen. Diese finden Sie unten im Dokumententenupload. Wir legen viel Wert auf eine sehr hohe Qualität, welche sich sowohl in unserem Logo als auch den Etiketten Wiederspiegeln soll.
Unsere Kundschaft ist hauptsächlich Ü35 und legt viel Wert auf hochwertige Produkte.
Aufgabenstellung
Eines direkt vorne weg: Da wir unsere komplette Produktpalette neu gestalten wollen würde ich Sie bitten, der Einfachheit halber zuerst nur ein Schnapsetikett (z.B. Zwetschge oder Willi), ein Likör Etikett und ein Etikett für unseren Whiskey zu erstellen.
Darüber hinaus bitte ich Sie auch ein Design für unseren neuen Gin und einen Aquavit, welcher im Herbst auf den Markt kommen soll zu designen. Im Anschluss daran, werde ich in der Zusammenarbeit mit Ihnen die Etiketten optimieren wollen.
Sobald ein 'Grundetikett' entstanden ist, sollen dann auch die anderen Schnäpse und Liköre in dem gleichen Stil erstellt werden. Explizit möchte ich daraufhin weisen, dass sowohl die Whiskeys als auch der Gin und der Aquavit nicht zwangsläufig das gleiche 'Grundetikett' wie der Schnaps und der Likör haben sollen. Ist bei unseren aktuellen Etiketten auch nicht der Fall. Sehen Sie in den Bildern unten.
Wir verkaufen unseren Schnaps und Likör in 3 unterschieldichen Größen 0,2; 0,5 und 1,0 Liter. Wir verwenden für die 0,2 und 0,5 die Flasche Tessa. Das Etikett der 0,5er Flasche soll in etwa 65x120-130 mm sein. Hier sind wir allerdings variabel.
Dieses entstandene Etikett soll dann auf die anderen Flaschen entsprechend angepasst werden.
Sie finden im Dokumentenupload unsere aktuellen Etiketten und das Logo, welches eingebaut werden soll. Auch ein Etikett von einem örtlichen Weingut, welches mir vom Aufbau und der Unterteilung sehr gut gefällt, werde ich mit anhängen. Allerdings ist dieses Bild sehr unscharf. Wie gesagt es geht hierbei hauptsächlich um die Einteilung mit den oberen und den unteren 'Rahmen'.
Auch unsere Preisliste finden Sie Anhang, wobei diese noch in der Rohform ist und das Obst so nicht verwendet wird, aber hier sind die meisten Produkte drauf.
Das Logo gibt es in verschiedenen Farben. Gerne dürfen Sie für die unterschiedlichen Produkte auch unterschiedliche Farben nutzen.
Was ich mir persönlich g..

```html
<!DOCTYPE html>
<html lang="de">
<head>
<meta charset="utf-8">
<title>Brunnacker's Zwetschge – Etikett</title>
<link rel="stylesheet" href="https://fonts.googleapis.com/css2?family=Cormorant+Garamond:wght@600&family=Montserrat:wght@500;600&family=Mulish:wght@400&display=swap">
<style>
  :root {
    --canvas: #e2e2e2;
    --plum: #5a5468;
    --cream: #efeeea;
    --paper: #f4f3f0;
    --gold: #b99a52;
    --ink: #3f3b49;
    --sketch-a: #dcdae0;
    --sketch-b: #c9c6d0;
  }
  * { margin: 0; padding: 0; box-sizing: border-box; }
  html, body { width: 1180px; height: 1200px; overflow: hidden; background: var(--canvas); }
  .label {
    position: absolute; left: 312px; top: 40px;
    width: 556px; height: 1120px;
    display: flex; flex-direction: column;
    box-shadow: 0 2px 10px rgba(0,0,0,.08);
  }
  .brand-band {
    height: 270px; background: var(--plum);
    display: flex; flex-direction: column; align-items: center; justify-content: flex-end;
    padding-bottom: 48px; gap: 26px;
  }
  .brand-dot { width: 64px; height: 64px; border-radius: 50%; background: var(--gold); }
  .brand-name {
    font-family: "Montserrat", sans-serif; font-weight: 600;
    font-size: 25px; letter-spacing: 6px; color: var(--gold);
  }
  .product {
    height: 611px; background: var(--cream); position: relative; text-align: center;
  }
  .product-title {
    font-family: "Cormorant Garamond", serif; font-weight: 600;
    font-size: 60px; line-height: 69px; letter-spacing: 6px; color: var(--gold);
    padding-top: 38px; text-transform: uppercase;
  }
  .product-sub {
    font-family: "Mulish", sans-serif; font-size: 20px; color: var(--ink);
    margin-top: 8px;
  }
  .fruit-sketch {
    position: absolute; left: 102px; top: 235px; width: 350px; height: 305px;
    border-radius: 46% 54% 48% 52%;
    background: radial-gradient(circle at 60% 40%, var(--sketch-b), var(--sketch-a) 70%, transparent 72%);
  }
  .facts {
    position: absolute; left: 30px; right: 36px; bottom: 18px;
    display: flex; justify-content: space-between;
    font-family: "Montserrat", sans-serif; font-weight: 600; font-size: 20px;
    color: var(--ink); letter-spacing: 1px;
  }
  .maker {
    height: 144px; background: var(--plum);
    display: flex; flex-direction: column; align-items: center; justify-content: center;
    font-family: "Montserrat", sans-serif; font-weight: 500; font-size: 16px;
    line-height: 20.5px; letter-spacing: 2.4px; color: var(--gold); text-transform: uppercase;
  }
  .spacer { height: 14px; background: var(--paper); }
  .lot {
    flex: 1; background: var(--cream);
    display: flex; align-items: center; justify-content: center;
    font-family: "Montserrat", sans-serif; font-weight: 600; font-size: 20px;
    color: var(--ink); letter-spacing: 1.5px;
  }
</style>
</head>
<body>
  <main class="label">
    <header class="brand-band">
      <span class="brand-dot"></span>
      <span class="brand-name">BRUNNACKER'S</span>
    </header>
    <section class="product">
      <h1 class="product-title">Brunnacker's<br>Zwetschge</h1>
      <p class="product-sub">Brunnacker's Birne im Holzfass gereift</p>
      <div class="fruit-sketch" role="img" aria-label="Kupferstich-Illustration einer halbierten und einer ganzen Zwetschge mit Blatt"></div>
      <div class="facts"><span>40% vol.</span><span>0,5 l</span></div>
    </section>
    <address class="maker">
      <span>Edelbrä &amp; Liköre</span>
      <span>Konrad Brunnacker</span>
      <span>Lindenweg 12</span>
      <span>D.97999 Talheim</span>
      <span>Tel. 09871 / 4412</span>
    </address>
    <div class="spacer"></div>
    <footer class="lot">1.07/06</footer>
  </main>
</body>
</html>
```